Bellmoor Glassware Brand Design

Logo Design Brief

Bellmoor Glassware is a startup premium drinkware company launching its first product - a premium grade 24oz Copa de Balon Gin Glass.

We are looking for branding design to produce our logo and the label for our first product; a premium 24oz Copa de Balon Gin Glass.

Design Brief for logo:

• Premium brand
• Modern, elegant and sleek design
• Not busy
• Logo does not have to include reference to drinkware

Label Design Brief:

A label design for our packaging - The packaging is tubular and will house 2 gin glasses for retail sale. The label will be stuck on the front of the tube and will need to excite people about the purchase they have just made with Bellmoor Glassware.
The label design needs to incorporate the logo and reflect our premium brand image.

• The label size is 460mm x 150mm

• Label must have modern and sleek look and must not look busy.

• The label will need to work well in both multicolour and single colour print.

• Please see attached Barcode, this will need to be incorporated into the label. Barcode will need to be 300dpi or higher and 381mm x 254mm to be scannable on the packaging.

• Please see attached pictures of the tubular packaging the label is going on to

Please also see attached 3 images of the glasses being sold - This is for reference only.

Design period has been extended for 5 Days, please ensure both a logo and corresponding packaging design is submitted. Thank you Added Wednesday, October 4, 2017

Target Market(s)

Gin Drinkers - Premium - Male and Female - All ages above 18

Industry/Entity Type

It Company

Logo Text

Bellmoor

Font styles to use
Serif
Sans Serif

Colors

Designer to choose colors to be used in the design.

Requirements
Must have
• Sleek modern design. Logo and Label must be submitted on this project.
Should not have
• Do not make this a busy logo or label

```html
<!DOCTYPE html>
<html lang="en">
<head>
<meta charset="utf-8">
<title>Bellmoor Glassware – Gin Glass Labels</title>
<link href="https://fonts.googleapis.com/css2?family=Jost:wght@300;400&display=swap" rel="stylesheet">
<style>
  :root {
    --page-bg: #ffffff;
    --kraft: #9b8770;
    --kraft-dark: #7f6c58;
    --ink-black: #262626;
    --cream: #ffffff;
    --copper: #c98a5c;
    --copper-deep: #8a4f2c;
    --copper-bright: #e07a35;
  }
  * { margin: 0; padding: 0; box-sizing: border-box; }
  html, body {
    width: 1185px; height: 1200px; overflow: hidden;
    background: var(--page-bg);
    font-family: "Jost", sans-serif;
  }
  .canvas { position: relative; width: 1185px; height: 1200px; }

  .label {
    position: absolute; top: 155px; width: 185px; height: 913px;
    background: var(--kraft);
  }
  .label--mono { left: 308px; color: var(--cream); }
  .label--copper { left: 663px; }

  .label__band {
    position: absolute; left: 0; top: 173px; width: 100%; height: 629px;
    background: var(--ink-black);
    color: var(--copper);
  }

  .brand {
    position: absolute; left: 0; width: 100%; text-align: center;
  }
  .brand__name {
    display: block; font-size: 16px; font-weight: 400; letter-spacing: 3.5px;
  }
  .brand__sub {
    display: block; font-size: 8.5px; font-weight: 400; letter-spacing: 2.5px; margin-top: 1px;
  }

  .product-title {
    position: absolute; left: 0; width: 100%; text-align: center;
    font-weight: 300; font-size: 64px; line-height: 60px; letter-spacing: -1px;
  }

  .artwork { position: absolute; left: 0; width: 100%; }

  .spec {
    position: absolute; width: 100%; text-align: center; font-weight: 300;
  }
  .spec__size { display: block; font-size: 22px; line-height: 24px; }
  .spec__pack { display: block; font-size: 15px; line-height: 20px; letter-spacing: -0.3px; }

  .label--mono .brand { top: 352px; }
  .label--mono .product-title { top: 382px; }
  .label--mono .artwork { top: 530px; height: 190px; }
  .label--mono .spec { top: 730px; }

  .label--copper .brand { top: 179px; }
  .label--copper .product-title { top: 208px; }
  .label--copper .artwork { top: 355px; height: 220px; }
  .label--copper .spec { top: 571px; left: 0; text-align: right; padding-right: 12px; }
  .label--copper .spec__size { color: var(--copper-bright); }
  .label--copper .spec__pack { color: var(--cream); }
</style>
</head>
<body>
<main class="canvas">

  <section class="label label--mono">
    <div class="brand">
      <span class="brand__name">BELLMOOR</span>
      <span class="brand__sub">GLASSWARE</span>
    </div>
    <h1 class="product-title">Gin<br>Glass</h1>
    <svg class="artwork" viewBox="0 0 185 190" preserveAspectRatio="none" role="img" aria-label="Diagonal band illustration of flowing botanical and wood-grain lines in white">
      <polygon points="0,70 185,0 185,110 0,190" fill="#f3efe9"/>
    </svg>
    <p class="spec">
      <span class="spec__size">24oz</span>
      <span class="spec__pack">DOUBLE-PACK</span>
    </p>
  </section>

  <section class="label label--copper">
    <div class="label__band">
      <div class="brand">
        <span class="brand__name">BELLMOOR</span>
        <span class="brand__sub">GLASSWARE</span>
      </div>
      <h2 class="product-title">Gin<br>Glass</h2>
      <svg class="artwork" viewBox="0 0 185 220" preserveAspectRatio="none" role="img" aria-label="Diagonal band illustration of flowing botanical and wood-grain lines in copper tones">
        <defs>
          <linearGradient id="copperFlow" x1="0" y1="1" x2="1" y2="0">
            <stop offset="0" stop-color="#8a4f2c"/>
            <stop offset="0.55" stop-color="#b36a3c"/>
            <stop offset="1" stop-color="#d9996a"/>
          </linearGradient>
        </defs>
        <polygon points="0,90 185,0 185,120 0,220" fill="url(#copperFlow)"/>
      </svg>
      <p class="spec">
        <span class="spec__size">24oz</span>
        <span class="spec__pack">DOUBLE-PACK</span>
      </p>
    </div>
  </section>

</main>
</body>
</html>
```